Homepage web design

I need a homepage design that will be easy to build into a default Word Press theme. Basically, header, navigation, body with sidebar, and footer.

This website is for a small commercial real estate firm in the Washington DC, Maryland and Virginia market.

THIS IS NOT A HOUSING/RESIDENTIAL WEBSITE. PLEASE DO NOT ADD ANY PROPERTY SEARCH FUNCTIONALITY.

Target Market(s)

People looking for basic information about the team and services provided.

Industry/Entity Type

Real Estate

Requirements
Must have
• Professional look. Clean design.

```html
<!DOCTYPE html>
<html lang="en">
<head>
<meta charset="utf-8">
<title>Quillmere Property Advisors</title>
<link rel="stylesheet" href="https://fonts.googleapis.com/css2?family=Open+Sans:wght@400;600;700&family=Open+Sans+Condensed:wght@300;700&family=Arimo:wght@400;700&display=swap">
<style>
:root{
  --green:#0b8549;
  --green-text:#0a7a42;
  --dark:#4a4a4a;
  --ink:#3d3d3d;
  --muted:#a9a9a9;
  --light-muted:#bdbdbd;
  --panel:#ffffff;
  --rule:#e2e2e2;
}
*{margin:0;padding:0;box-sizing:border-box}
html,body{width:1177px;height:1200px;overflow:hidden}
body{font-family:"Arimo",Arial,sans-serif;color:var(--ink);background:#f1f2f1}
.page{position:relative;width:1177px;height:1200px;overflow:hidden}
.backdrop{position:absolute;inset:0;background:linear-gradient(120deg,#dfe3e1 0%,#f6f6f6 45%,#d9dcdb 75%,#eeeeee 100%)}
.top-rule{position:absolute;left:0;top:0;width:1177px;height:5px;background:var(--green)}
.panel{position:absolute;background:var(--panel)}
.photo{position:absolute}
.header{left:94px;top:5px;width:981px;height:101px}
.brand{position:absolute;left:16px;top:44px;display:flex;align-items:center;gap:9px}
.brand-mark{width:12px;height:12px;background:var(--green)}
.brand-name{font-family:"Arimo",sans-serif;font-weight:700;color:var(--green);font-size:22px;line-height:1}
.social{position:absolute;right:20px;top:46px;display:flex;gap:9px}
.social span{width:18px;height:18px;border-radius:50%;background:var(--dark)}
.nav{position:absolute;left:94px;top:106px;width:981px;height:46px;background:var(--dark);display:flex;align-items:center;padding-left:34px;gap:25px}
.nav a{font-family:"Open Sans Condensed","Open Sans",sans-serif;font-weight:700;color:#fff;text-decoration:none;font-size:16px;text-transform:uppercase}
.hero{left:94px;top:155px;width:682px;height:372px;background:linear-gradient(180deg,#3f72c4 0%,#7ba5dc 32%,#e2e0d8 45%,#cfc9bb 70%,#3f6b24 88%,#2f5a1b 100%)}
.dots{position:absolute;left:685px;top:504px;display:flex;gap:9px}
.dots span{width:11px;height:11px;border-radius:50%;background:#fff}
.properties{left:780px;top:155px;width:295px;height:372px}
.panel-title{font-family:"Open Sans Condensed","Open Sans",sans-serif;font-weight:700;font-size:17px;color:var(--ink);text-transform:uppercase}
.properties .panel-title{position:absolute;left:92px;top:5px}
.prop{position:absolute;left:7px;width:280px;height:100px}
.prop .thumb{position:absolute;left:0;top:0;width:98px;height:97px}
.prop h3{position:absolute;left:110px;top:0;font-size:13px;font-weight:700;color:var(--green-text);line-height:17px;width:150px}
.prop p{position:absolute;left:110px;font-size:10px;line-height:18px;color:var(--light-muted);width:148px}
.prop p a{color:var(--green-text);text-decoration:none}
.services{left:94px;top:535px;width:680px;height:413px}
.services .panel-title{position:absolute;left:34px;top:20px;font-size:16px}
.services .rule{position:absolute;left:15px;top:42px;width:665px;height:2px;background:var(--rule)}
.service{position:absolute;top:57px;width:210px;height:340px}
.service h3{position:absolute;font-size:14px;font-weight:700;color:var(--green-text);letter-spacing:.3px;white-space:nowrap}
.service p{position:absolute;font-size:11.5px;line-height:17px;color:var(--ink);width:195px}
.btn{position:absolute;width:79px;height:33px;background:var(--dark);color:#fff;font-size:13.5px;display:flex;align-items:center;justify-content:center;font-family:"Open Sans",sans-serif}
.who{position:absolute;left:780px;top:535px;width:295px;height:179px;background:var(--green);color:#fff}
.who h2{position:absolute;left:23px;top:11px;font-family:"Open Sans",sans-serif;font-weight:400;font-size:18px}
.who .rule{position:absolute;left:19px;top:37px;width:227px;height:1px;background:rgba(255,255,255,.35)}
.who .lead{position:absolute;left:19px;top:43px;font-size:14.5px;line-height:17px;width:260px}
.who p{position:absolute;left:17px;top:88px;font-size:10.5px;line-height:18px;width:235px;color:#e2f1e8}
.gallery{left:782px;top:719px;width:291px;height:229px}
.gallery .panel-title{position:absolute;left:15px;top:6px;font-family:"Arimo",sans-serif;font-size:13.5px;font-weight:400}
.gallery .thumb{position:absolute;width:91px;height:82px}
.gallery .more{position:absolute;left:235px;top:202px;font-size:12px;font-weight:700;color:var(--ink);font-family:"Open Sans",sans-serif}
.footer-col{position:absolute}
.footer-col h4{font-family:"Arimo",sans-serif;font-weight:700;font-size:13px;color:#555;text-transform:uppercase;margin-bottom:15px}
.footer-col li{list-style:none;font-size:12px;line-height:19.6px;color:var(--muted);font-weight:700;opacity:.8}
.contact{position:absolute;left:786px;top:975px}
.contact h4{font-family:"Arimo",sans-serif;font-weight:700;font-size:13px;color:#555;text-transform:uppercase}
.contact .hello{font-size:14.5px;margin-top:3px}
.contact .phone{font-family:"Arimo",sans-serif;font-size:19px;color:var(--green-text);margin-top:38px}
.contact .email{font-size:12.5px;font-weight:700;margin-top:2px}
.bottom-bar{position:absolute;left:0;top:1137px;width:1177px;height:63px;background:var(--dark);color:#e6e6e6;font-size:12px;line-height:14px;padding:23px 0 0 110px}
.bottom-bar span{margin:0 9px}
</style>
</head>
<body>
<div class="page">
  <div class="backdrop" role="img" aria-label="Softly blurred bright interior of a modern room behind the page"></div>
  <div class="top-rule"></div>

  <header class="panel header">
    <div class="brand"><span class="brand-mark"></span><span class="brand-name">Quillmere Property Advisors</span></div>
    <div class="social"><span></span><span></span><span></span><span></span></div>
  </header>

  <nav class="nav">
    <a href="#">Home</a><a href="#">About Us</a><a href="#">Services</a><a href="#">Gallery</a><a href="#">Blog</a><a href="#">Testimonials</a><a href="#">Contact Us</a>
  </nav>

  <div class="photo hero" role="img" aria-label="Modern white curved building with lit windows, palm trees and a green lawn at dusk"></div>
  <div class="dots"><span></span><span></span><span></span><span></span></div>

  <aside class="panel properties">
    <div class="panel-title">Our Properties</div>
    <div class="prop" style="top:34px">
      <div class="thumb photo" role="img" aria-label="Stone and siding house with front porch" style="background:linear-gradient(180deg,#dfe6ea,#8d8478 55%,#4f7a32)"></div>
      <h3>Praesent vestibulum molestie lacus</h3>
      <p style="top:42px">Praesent vestibulum molestie lacus. Aenean nonummy hen drerit mauris.</p>
    </div>
    <div class="prop" style="top:150px">
      <div class="thumb photo" role="img" aria-label="House among pine trees with a wide lawn" style="background:linear-gradient(180deg,#4a7fc9,#9fbfe4 40%,#3e6b2a 60%,#5a9a3a)"></div>
      <h3>Praesent vestibulum molestie lacus</h3>
      <p style="top:36px">Praesent vestibulum molestie lacus. Aenean nonummy hen drerit mauris.</p>
    </div>
    <div class="prop" style="top:268px">
      <div class="thumb photo" role="img" aria-label="Dark timber-frame house with garages" style="background:linear-gradient(180deg,#6a95d0,#e8e3dc 45%,#3b3430 75%,#5c5a55)"></div>
      <h3>Praesent vestibulum molestie lacus</h3>
      <p style="top:36px">Praesent vestibulum molestie lacus. Aenean nonummy hen drerit mauris. <a href="#">Read More....</a></p>
    </div>
  </aside>

  <section class="panel services">
    <div class="panel-title">Our Services</div>
    <div class="rule"></div>
    <div class="service" style="left:34px">
      <div class="photo" role="img" aria-label="Suburban house with double garage and trees" style="left:0;top:0;width:194px;height:193px;background:linear-gradient(180deg,#6ea1dc,#5e8a3c 30%,#d8c8a8 55%,#cfc8bd 80%,#4f8a2c)"></div>
      <h3 style="left:0;top:205px">Buying Home</h3>
      <p style="left:1px;top:238px">Lorem ipsum dolor sit amet, consec tetur adipisicing elit, sed do eiusm od tempor incididunt</p>
      <div class="btn" style="left:1px;top:304px">MORE</div>
    </div>
    <div class="service" style="left:242px">
      <div class="photo" role="img" aria-label="Modern brick building with a cantilevered block over a lawn" style="left:0;top:0;width:197px;height:195px;background:linear-gradient(90deg,#8a4a36 0%,#9b5640 50%,#a9c9ea 52%,#3f6d2a 90%)"></div>
      <h3 style="left:3px;top:210px">Luxury Property</h3>
      <p style="left:0;top:243px">Lorem ipsum dolor sit amet, consec tetur adipisicing elit, sed do eiusm od tempor incididunt</p>
      <div class="btn" style="left:1px;top:304px">MORE</div>
    </div>
    <div class="service" style="left:459px">
      <div class="photo" role="img" aria-label="Pale concrete facade with a window and glass wall" style="left:0;top:0;width:198px;height:199px;background:linear-gradient(180deg,#d8d6cf,#c8c5bb 70%,#6b8a5c 85%,#4a5a50)"></div>
      <h3 style="left:0;top:210px">Selling Home</h3>
      <p style="left:0;top:243px">Lorem ipsum dolor sit amet, consec tetur adipisicing elit, sed do eiusm od tempor incididunt</p>
      <div class="btn" style="left:-6px;top:304px">MORE</div>
    </div>
  </section>

  <aside class="who">
    <h2>WHO WE ARE</h2>
    <div class="rule"></div>
    <div class="lead">Praesent vestibulum molestie lacus. Aenean nonummy hendrerit</div>
    <p>Praesent vestibulum molestie lacus. Aenean nonummy hendrerit mauris. Phasellus porta. Fusce suscipit varius mi. Cum sociis natoque penatibus et magnis dis parturient montes.</p>
  </aside>

  <aside class="panel gallery">
    <div class="panel-title">GALLERY</div>
    <div class="thumb photo" role="img" aria-label="Apartment complex under blue sky" style="left:15px;top:29px;background:linear-gradient(180deg,#5d8fd3,#8a6a55 45%,#5a8a3a)"></div>
    <div class="thumb photo" role="img" aria-label="Balcony terrace overlooking water" style="left:129px;top:29px;width:95px;background:linear-gradient(90deg,#6d5a48,#b8b6b0 50%,#7aa2c8)"></div>
    <div class="thumb photo" role="img" aria-label="Bright sunroom with seating" style="left:17px;top:124px;background:linear-gradient(180deg,#f0efea,#d9d6cf 60%,#6a5a4a)"></div>
    <div class="thumb photo" role="img" aria-label="Large house with landscaped garden" style="left:130px;top:124px;width:94px;background:linear-gradient(180deg,#8fb1de,#c8b89a 45%,#4d7a2e)"></div>
    <div class="more">More »</div>
  </aside>

  <div class="footer-col" style="left:109px;top:975px">
    <h4>Featured Links</h4>
    <ul><li>Praesent vestibulum</li><li>Molestie lacus</li><li>Aenn nommy hendrerit</li><li>Phasellus porta</li><li>Fusce suscipit varius mi</li></ul>
  </div>
  <div class="footer-col" style="left:337px;top:970px">
    <h4 style="margin-bottom:22px">Partners &amp; Sponsors</h4>
    <ul><li>Praesent vestibulum</li><li>Molestie lacus</li><li>Aenn nommy hendrerit</li><li>Phasellus porta</li><li>Fusce suscipit varius mi</li></ul>
  </div>
  <div class="footer-col" style="left:547px;top:970px">
    <h4 style="margin-bottom:22px">Recent Articles</h4>
    <ul><li>Praest vestibulum molestie</li><li>Donec tempor libero</li><li>Etiam dictum egestas</li></ul>
  </div>
  <div class="contact">
    <h4>Our Properties Questions?</h4>
    <div class="hello">We're happy to help!</div>
    <div class="phone">1-800-555-01-29</div>
    <div class="email">mail@quillmere.example</div>
  </div>

  <footer class="bottom-bar">
    Copyright 2013. All rights reserved.<br>
    Terms &amp; Conditions<span>-</span>Privacy<span>-</span>Disclaimer
  </footer>
</div>
</body>
</html>
```